Real Estate Agency Chatterlane Cover Photo

We need a Chatterlane cover photo created for our Real Estate Business. We also need this cover photo adapted to several other platforms. Please read this brindlo doc for full specifications of the job https://files.brindlo-example.net/sheet/d/8QwerPLm4ZxVb2NnKs7RtYhUe3_gHdjAoFcWsMvBn/view?mode=share

Please also carefully read the Must Haves/Should Not Haves

Please contact me if you have any queries. Looking forward to seeing your designs!

Owen

Industry/Entity Type

Real Estate Agent

Requirements
Must have
• The Taglines 'More Money In Your Pocket' and sub tagline 'With Our Low Flat Fee To Sell Your Home'

It can then also have other elements e.g our logo, contact details and anything else you think will work well.

It must also have great graphic design work which looks custom and very clean/modern
Should not have
• Must not have poor quality stock images or anything tacky regarding money etc

```html
<!DOCTYPE html>
<html lang="en">
<head>
<meta charset="utf-8">
<title>Norvel Cover</title>
<link href="https://fonts.googleapis.com/css2?family=Open+Sans:wght@400;600;700&display=swap" rel="stylesheet">
<style>
  :root{
    --stage:#a4a3a4;
    --paper:#e9e8e9;
    --charcoal:#202020;
    --red:#e3141c;
    --red-deep:#8e0f17;
    --red-mid:#c0141a;
    --white:#ffffff;
    --shade:rgba(40,40,40,.62);
  }
  *{margin:0;padding:0;box-sizing:border-box}
  html,body{width:1200px;height:960px;overflow:hidden}
  body{background:var(--stage);font-family:"Open Sans",Arial,sans-serif;position:relative}
  .cover{position:absolute;left:40px;top:267px;width:1120px;height:426px;background:var(--paper);overflow:hidden;box-shadow:0 10px 30px rgba(0,0,0,.25)}
  .cover-shapes{position:absolute;inset:0;width:100%;height:100%}
  .brand-name{position:absolute;left:80px;top:96px;font-size:82px;font-weight:600;color:var(--red);letter-spacing:2px;line-height:1}
  .tagline{position:absolute;left:80px;top:196px;font-size:30px;font-weight:400;color:var(--white);line-height:1}
  .sub-tagline{position:absolute;left:80px;top:240px;width:352px;height:30px;background:var(--white);color:var(--red);font-size:17px;font-weight:400;line-height:30px;padding-left:18px}
  .website{position:absolute;left:220px;top:330px;width:440px;text-align:center;font-size:27px;color:var(--white);line-height:1}
  .steps{position:absolute;left:690px;top:322px;width:420px;text-align:center;color:var(--white);line-height:1}
  .steps-title{font-size:19px;font-weight:400;margin-bottom:12px}
  .steps-list{font-size:12px;letter-spacing:.3px}
  .call{position:absolute;right:28px;top:34px;text-align:right;line-height:1}
  .call-label{font-size:32px;font-weight:600;color:var(--white)}
  .call-number{font-size:21px;color:var(--red);margin-top:8px}
</style>
</head>
<body>
  <section class="cover">
    <svg class="cover-shapes" viewBox="0 0 1120 426" xmlns="http://www.w3.org/2000/svg">
      <defs>
        <linearGradient id="photoTone" x1="0" y1="0" x2="1" y2="1">
          <stop offset="0" stop-color="#c9d2c6"/>
          <stop offset=".35" stop-color="#7d8f4e"/>
          <stop offset=".7" stop-color="#5b6b34"/>
          <stop offset="1" stop-color="#3f4a26"/>
        </linearGradient>
        <linearGradient id="webBand" x1="0" y1="0" x2="1" y2="0">
          <stop offset="0" stop-color="#8a0f16"/>
          <stop offset="1" stop-color="#dc1c24"/>
        </linearGradient>
        <linearGradient id="stepsBand" x1="0" y1="0" x2="1" y2="0">
          <stop offset="0" stop-color="#7e0a10"/>
          <stop offset=".6" stop-color="#c0141a"/>
          <stop offset="1" stop-color="#8e0f17"/>
        </linearGradient>
      </defs>
      <polygon class="photo-area" role="img" aria-label="Photo of the two agents standing outdoors in front of a bushland valley view" points="430,0 1120,0 1120,300 700,300 620,330" fill="url(#photoTone)"/>
      <polygon class="photo-shade" points="900,0 1120,0 1120,300 1080,300" fill="var(--shade)"/>
      <polygon class="accent-triangle" points="370,52 420,2 450,52" fill="var(--red-mid)"/>
      <polygon class="dark-panel" points="0,52 440,52 615,312 0,312" fill="var(--charcoal)"/>
      <polygon class="web-band" points="185,312 720,298 650,400 265,400" fill="url(#webBand)"/>
      <polygon class="dark-sliver" points="640,400 650,400 680,360 690,426 615,426" fill="var(--charcoal)"/>
      <polygon class="steps-band" points="740,298 1120,298 1120,426 650,426" fill="url(#stepsBand)"/>
      <polygon class="steps-edge" points="720,298 740,298 660,414 648,410" fill="#7a1218"/>
    </svg>

    <div class="brand-name">NORVEL</div>
    <div class="tagline">More Money In Your Pocket</div>
    <div class="sub-tagline">With Our Low Flat Fee To Sell Your Home</div>
    <div class="website">www.norvel-homes.com.au</div>

    <div class="steps">
      <div class="steps-title">5 EASY STEPS TO SELL YOUR HOME</div>
      <div class="steps-list">APPRAISAL | ENGAGEMENT | ADVERTISEMENT | INSPECTIONS | SETTLEMENT</div>
    </div>

    <div class="call">
      <div class="call-label">Call Us</div>
      <div class="call-number">+61 2 5550 1947</div>
    </div>
  </section>
</body>
</html>
```